Create a Modern, On-Brand Zoom Background for Our LUMORA Webinar Team

Project Overview
We are hosting a Zoom webinar next month and want all team members to appear unified on-screen. We need a custom, branded Zoom background that incorporates our corporate identity while remaining clean, modern, and visually polished.
Design Requirements
File Type: Static image (no motion) optimized for Zoom virtual backgrounds
Orientation: 16:9 landscape
Main Logo: KALDRIN (primary)
Secondary Logo: LUMORA (supporting logo)
Design Style:
Clean, crisp, modern
Professional and easy on the eyes
Eye-catching but not busy or distracting
Bold enough to look strong on-camera but minimal enough to sit behind presenters
Color Palette: Use Kaldrin brand colors, LUMORA colors, or a subtle combination
Avoid: Clutter, heavy textures, distracting patterns, excessive gradients, motion effects
Preferred (Not Required)
Designs created in Canva are strongly preferred.
Designers who provide:
Editable Canva link
…will be prioritized, as this allows us to make future updates easily.
Deliverables
Final Zoom-ready JPG/PNG background
Source files (Canva preferred; AI/PSD acceptable)
Audience & Use Case
This background will be used by internal Kaldrin team members during a high-visibility webinar with physicians and clinical partners involved in the LUMORA study.

```html
<!DOCTYPE html>
<html lang="en">
<head>
<meta charset="utf-8">
<title>Kaldrin Webinar Background</title>
<link href="https://fonts.googleapis.com/css2?family=Oswald:wght@300;500&display=swap" rel="stylesheet">
<style>
  :root {
    --navy-deep: #07163f;
    --navy-mid: #0c2a6b;
    --navy-edge: #0a1a45;
    --brand-green: #6db33f;
    --white: #ffffff;
    --helix-tint: rgba(120, 145, 200, 0.28);
  }
  html, body {
    margin: 0;
    padding: 0;
    width: 1200px;
    height: 675px;
    overflow: hidden;
    background: var(--navy-deep);
  }
  .zoom-background {
    position: relative;
    width: 1200px;
    height: 675px;
    overflow: hidden;
    font-family: "Oswald", sans-serif;
  }
  .backdrop-photo {
    position: absolute;
    inset: 0;
    background:
      radial-gradient(ellipse at 38% 8%, var(--navy-mid) 0%, rgba(12, 42, 107, 0) 60%),
      linear-gradient(160deg, var(--navy-mid) 0%, var(--navy-edge) 55%, var(--navy-deep) 100%);
  }
  .helix-decoration {
    position: absolute;
    left: 0;
    top: 0;
    width: 310px;
    height: 675px;
    background: linear-gradient(90deg, var(--helix-tint) 0%, rgba(120, 145, 200, 0.12) 70%, rgba(120, 145, 200, 0) 100%);
  }
  .primary-logo {
    position: absolute;
    right: 56px;
    top: 66px;
    text-align: right;
    color: var(--brand-green);
    font-weight: 300;
    line-height: 1;
  }
  .primary-logo .brand-name {
    display: block;
    font-size: 96px;
    letter-spacing: -1px;
  }
  .primary-logo .brand-division {
    display: block;
    font-size: 20px;
    letter-spacing: 0.5px;
    margin-top: 4px;
  }
  .study-logo {
    position: absolute;
    right: 55px;
    top: 568px;
    text-align: right;
    color: var(--white);
    font-weight: 500;
    line-height: 1;
  }
  .study-logo .study-name {
    display: block;
    font-size: 44px;
    letter-spacing: 0.5px;
  }
  .study-logo .study-tagline {
    display: block;
    font-size: 6px;
    margin-top: 3px;
    white-space: nowrap;
  }
</style>
</head>
<body>
  <main class="zoom-background">
    <div class="backdrop-photo" role="img" aria-label="Upward view of a glass office tower tinted in deep navy blue"></div>
    <div class="helix-decoration" role="img" aria-label="Large faint decorative helix along the left edge"></div>

    <div class="primary-logo">
      <span class="brand-name">KALDRIN</span>
      <span class="brand-division">BIOLOGICS</span>
    </div>

    <div class="study-logo">
      <span class="study-name">LUMORA U.S.</span>
      <span class="study-tagline">Solvia Disc NP Randomized, Sham-Controlled, Multi-Center, Double Blind Clinical Trial</span>
    </div>
  </main>
</body>
</html>
```